Gourmet cookie company needs a label designed

We need a label designed for a new cookie company. We make mini cookies. The labels will be placed on either white tins or clear containers. We would like some bright and eye catching label although not child like. Our target customer is adults not kids.
Any color/colors acceptable. The initial label will be a square 4" label but the design should also be able to be formatted to fit on a round label as well in the future.

Text on label: Rosalind's Wafer Crumb Company; Chocolate Chip; All Natural; New Wt. 8.0oz

```html
<!DOCTYPE html>
<html lang="en">
<head>
<meta charset="utf-8">
<title>Rosalind's Wafer Crumb Company – Chocolate Chip Labels</title>
<link rel="stylesheet" href="https://fonts.googleapis.com/css2?family=Marcellus&family=Chewy&family=Open+Sans:wght@400;700&display=swap">
<style>
  :root {
    --cream: #f2d79a;
    --plum: #551560;
    --white: #ffffff;
    --red: #d81f1f;
    --rust: #8c3c22;
    --cocoa: #8a4a2e;
    --biscuit: #d9a467;
    --biscuit-dark: #a8713d;
    --caption: #333333;
  }
  html, body {
    margin: 0;
    padding: 0;
    width: 1200px;
    height: 900px;
    overflow: hidden;
    background: var(--white);
  }
  .sheet {
    position: relative;
    width: 1200px;
    height: 900px;
    margin: 0;
  }
  .label {
    position: absolute;
    display: block;
  }
  .label--main { left: 104px; top: 152px; width: 594px; height: 594px; }
  .label--square { left: 816px; top: 85px; width: 288px; height: 288px; }
  .label--round { left: 817px; top: 524px; width: 288px; height: 288px; }
  .caption {
    position: absolute;
    margin: 0;
    width: 288px;
    text-align: center;
    font-family: "Open Sans", sans-serif;
    font-size: 12px;
    line-height: 16px;
    letter-spacing: 0.5px;
    color: var(--caption);
  }
  .caption--square { left: 816px; top: 382px; }
  .caption--round { left: 817px; top: 818px; }
  .brand-name { font-family: "Marcellus", serif; fill: var(--white); }
  .flavour {
    font-family: "Chewy", sans-serif;
    fill: var(--cocoa);
    stroke: var(--white);
    stroke-width: 6px;
    paint-order: stroke;
    stroke-linejoin: round;
  }
  .badge-text { font-family: "Marcellus", serif; fill: var(--white); font-weight: 700; }
  .weight { font-family: "Open Sans", sans-serif; font-weight: 700; fill: var(--white); }
</style>
</head>
<body>
<main class="sheet">
  <svg width="0" height="0" style="position:absolute" aria-hidden="true">
    <defs>
      <linearGradient id="red-field" x1="0" y1="0" x2="1" y2="0">
        <stop offset="0" stop-color="#8c3c22"/>
        <stop offset="0.3" stop-color="#d81f1f"/>
        <stop offset="0.7" stop-color="#d81f1f"/>
        <stop offset="1" stop-color="#8c3c22"/>
      </linearGradient>
      <radialGradient id="cookie-tone" cx="0.4" cy="0.55" r="0.7">
        <stop offset="0" stop-color="#d9a467"/>
        <stop offset="1" stop-color="#a8713d"/>
      </radialGradient>
      <clipPath id="round-cut">
        <circle cx="297" cy="297" r="297"/>
      </clipPath>
      <symbol id="label-art" viewBox="0 0 594 594">
        <rect class="label-base" width="594" height="594" fill="#f2d79a"/>
        <rect class="brand-rule" y="50" width="594" height="4" fill="#551560"/>
        <rect class="brand-band" y="58" width="594" height="81" fill="#551560"/>
        <rect class="brand-rule" y="143" width="594" height="4" fill="#551560"/>
        <text class="brand-name" x="297" y="104" text-anchor="middle" font-size="40" font-family="Marcellus, serif" fill="#ffffff">Rosalind’s</text>
        <text class="brand-name" x="297" y="129" text-anchor="middle" font-size="20" font-family="Marcellus, serif" fill="#ffffff">Wafer Crumb Company</text>
        <path class="red-field" d="M0 213 C 110 222, 220 330, 300 345 C 400 362, 520 335, 594 330 L594 594 L0 594 Z" fill="url(#red-field)"/>
        <rect class="cookie-photo" role="img" aria-label="Photo of a stack of chocolate chip cookies" x="256" y="332" width="296" height="212" rx="96" fill="url(#cookie-tone)"/>
        <g class="flavour-title">
          <text class="flavour" x="295" y="260" text-anchor="middle" font-size="80" textLength="450" lengthAdjust="spacingAndGlyphs" transform="rotate(-15 295 260)" font-family="Chewy, sans-serif" fill="#8a4a2e" stroke="#ffffff" stroke-width="6" paint-order="stroke" stroke-linejoin="round">Chocolate</text>
          <text class="flavour" x="302" y="318" text-anchor="middle" font-size="80" textLength="190" lengthAdjust="spacingAndGlyphs" transform="rotate(-14 302 318)" font-family="Chewy, sans-serif" fill="#8a4a2e" stroke="#ffffff" stroke-width="6" paint-order="stroke" stroke-linejoin="round">Chip</text>
        </g>
        <g class="natural-badge">
          <ellipse cx="162" cy="438" rx="54" ry="22" fill="none" stroke="#ffffff" stroke-width="4"/>
          <text class="badge-text" x="162" y="444" text-anchor="middle" font-size="17" font-family="Marcellus, serif" font-weight="700" fill="#ffffff">All Natural</text>
        </g>
        <text class="weight" x="297" y="553" text-anchor="middle" font-size="13" font-family="Open Sans, sans-serif" font-weight="700" fill="#ffffff">NET WT.</text>
        <text class="weight" x="297" y="570" text-anchor="middle" font-size="13" font-family="Open Sans, sans-serif" font-weight="700" fill="#ffffff">8.0 oz</text>
      </symbol>
    </defs>
  </svg>

  <svg class="label label--main" viewBox="0 0 594 594" role="img" aria-label="Chocolate Chip label, main artwork">
    <use href="#label-art" width="594" height="594"/>
  </svg>

  <svg class="label label--square" viewBox="0 0 594 594" role="img" aria-label="4 by 4 inch square label">
    <use href="#label-art" width="594" height="594"/>
  </svg>
  <p class="caption caption--square">4”x4” Square Label</p>

  <svg class="label label--round" viewBox="0 0 594 594" role="img" aria-label="4 by 4 inch round label">
    <g clip-path="url(#round-cut)">
      <use href="#label-art" width="594" height="594"/>
    </g>
  </svg>
  <p class="caption caption--round">4”x4” Round Label</p>
</main>
</body>
</html>
```